Business card for Harbor Crafters
Looking for creativity
Professional
Dominic Farrow
Owner Operator
47 S Pell Avenue
Larkfield, ME 19842
@domfarrow
craftharborco@mailvane.com
www.craftharborco.com
Looking for a creative business card for my company. I have a logo and like the feel of it. The business card should have a contemporary feel and be interesting.
The name of the company and the website

```html
<!DOCTYPE html>
<html lang="en">
<head>
<meta charset="UTF-8">
<title>Harbor Crafters — Business Card</title>
<link href="https://fonts.googleapis.com/css2?family=Caladea:wght@400;700&display=swap" rel="stylesheet">
<style>
  :root {
    --backdrop: #e9e6e1;
    --card: #ffffff;
    --brand-blue: #1f5fae;
    --ink: #2f3236;
    --muted: #5b5f64;
    --rule: #c9ccd0;
  }
  * { box-sizing: border-box; margin: 0; padding: 0; }
  html, body {
    width: 1200px;
    height: 780px;
    overflow: hidden;
    background: var(--backdrop);
    font-family: "Caladea", "Cambria", serif;
  }
  .stage {
    width: 1200px;
    height: 780px;
    display: flex;
    align-items: center;
    justify-content: center;
  }
  .card {
    position: relative;
    width: 1000px;
    height: 572px;
    background: var(--card);
    border-radius: 34px;
    overflow: hidden;
    box-shadow: 0 6px 24px rgba(0,0,0,0.12);
  }
  .card__stripe {
    position: absolute;
    left: 0; top: 0; bottom: 0;
    width: 46px;
    background: var(--brand-blue);
  }
  .card__stripe::after {
    content: "";
    position: absolute;
    top: 0; bottom: 0;
    left: 30px;
    width: 3px;
    background: var(--card);
  }
  .brand {
    position: absolute;
    top: 118px;
    left: 46px;
    right: 0;
    display: flex;
    align-items: center;
    justify-content: center;
    gap: 22px;
  }
  .brand__mark {
    width: 30px;
    height: 30px;
    background: var(--brand-blue);
  }
  .brand__name {
    font-size: 74px;
    font-weight: 400;
    color: var(--brand-blue);
    letter-spacing: 0.04em;
    text-transform: uppercase;
    line-height: 1;
    white-space: nowrap;
  }
  .details {
    position: absolute;
    top: 330px;
    left: 46px;
    right: 0;
    display: flex;
    justify-content: center;
  }
  .person {
    width: 330px;
    text-align: right;
    padding-right: 30px;
    border-right: 2px solid var(--rule);
    white-space: nowrap;
  }
  .person__name {
    font-size: 33px;
    font-weight: 700;
    color: var(--brand-blue);
    line-height: 1.1;
  }
  .person__role {
    font-size: 22px;
    color: var(--muted);
    margin-top: 4px;
    margin-bottom: 16px;
  }
  .person__address {
    font-style: normal;
    font-size: 23px;
    color: var(--ink);
    line-height: 1.3;
  }
  .contact {
    list-style: none;
    padding-left: 30px;
    width: 420px;
  }
  .contact__item {
    display: flex;
    align-items: center;
    gap: 14px;
    font-size: 22px;
    color: var(--ink);
    line-height: 1.55;
    white-space: nowrap;
  }
  .contact__icon {
    width: 20px;
    height: 20px;
    flex: none;
    fill: var(--brand-blue);
  }
</style>
</head>
<body>
  <main class="stage">
    <article class="card">
      <div class="card__stripe"></div>

      <header class="brand">
        <span class="brand__mark"></span>
        <h1 class="brand__name">Harbor Crafters</h1>
      </header>

      <section class="details">
        <div class="person">
          <p class="person__name">Dominic Farrow</p>
          <p class="person__role">Owner Operator</p>
          <address class="person__address">47 S Pell Avenue<br>Larkfield, ME 19842</address>
        </div>

        <ul class="contact">
          <li class="contact__item">
            <svg class="contact__icon" viewBox="0 0 20 20" aria-hidden="true">
              <path d="M4.5 1.5 7.5 5 6 7.5c1 2.5 3.5 5 6.5 6.5L15 12.5l3.5 3-1.5 3c-7 0-15-8-15-15z"/>
            </svg>
            610.555.0148
          </li>
          <li class="contact__item">
            <svg class="contact__icon" viewBox="0 0 20 20" aria-hidden="true">
              <circle cx="10" cy="10" r="8"/>
            </svg>
            @domfarrow
          </li>
          <li class="contact__item">
            <svg class="contact__icon" viewBox="0 0 20 20" aria-hidden="true">
              <path d="M1.5 4h17v12h-17z M3 5.5 10 11l7-5.5" stroke="#fff" stroke-width="1.4" stroke-linejoin="round"/>
            </svg>
            craftharborco@mailvane.com
          </li>
          <li class="contact__item">
            <svg class="contact__icon" viewBox="0 0 20 20" aria-hidden="true">
              <circle cx="10" cy="10" r="8.5"/>
              <path d="M1.5 10h17M10 1.5c3 3 3 14 0 17M10 1.5c-3 3-3 14 0 17M3.5 5.5h13M3.5 14.5h13" stroke="#fff" stroke-width="1.1" fill="none"/>
            </svg>
            www.craftharborco.com
          </li>
        </ul>
      </section>
    </article>
  </main>
</body>
</html>
```